Brightvale Mortgage - Banner Ads for Re-Marketing Campaigns

Need a banner ad for a retargeting Campaign with Kestrel Reach.

We would like to incorporate our attached logo. Also would like to incorporate a call to action "Pre-Qualify for a home loan today" and a button to click. This banner is to encourage previous customers to come back to our website and submit information. It must look good on mobile and desktop.

Our website is BrightvaleMortgage.example

Target Market(s)

Customers Seeking a Mortgage Loan

Industry/Entity Type

Mortgage

Requirements
Must have
• We would like the same basic design in the 4 sizes below.
• 728 pixels by 90 pixels leaderboard
• 300 by 250 medium rectangle
• 300 by 600 half page
• 320 by 100 mobile banner
Nice to have
• a Call to action, a button to click, animation
Should not have
• We are open.

```html
<!DOCTYPE html>
<html lang="en">
<head>
<meta charset="UTF-8">
<title>Brightvale Mortgage – Pre-Qualify Half Page Banner</title>
<link rel="stylesheet" href="https://fonts.googleapis.com/css2?family=Lato:wght@400;700;900&display=swap">
<style>
  :root {
    --header-bg: #ffffff;
    --panel-bg: #131618;
    --brand-navy: #1d4f9a;
    --sky-blue: #4ab3ea;
    --sun-yellow: #f6d31d;
    --button-blue: #1c5ea8;
    --white: #ffffff;
    --divider: #3b3a2c;
    --url-grey: #e6e6e6;
  }
  * { margin: 0; padding: 0; box-sizing: border-box; }
  html, body {
    width: 1200px;
    height: 2396px;
    overflow: hidden;
    background: var(--panel-bg);
    font-family: "Lato", Arial, sans-serif;
  }
  .banner {
    position: relative;
    width: 1200px;
    height: 2396px;
    background: var(--panel-bg);
    overflow: hidden;
  }
  .brand-header {
    position: absolute;
    inset: 0 0 auto 0;
    height: 420px;
    background: var(--header-bg);
    display: flex;
    align-items: center;
    justify-content: center;
    gap: 48px;
  }
  .brand-dot {
    width: 150px;
    height: 150px;
    border-radius: 50%;
    background: var(--sun-yellow);
  }
  .brand-name {
    color: var(--brand-navy);
    font-weight: 700;
    font-size: 96px;
    line-height: 1.0;
    letter-spacing: 3px;
    text-transform: uppercase;
  }
  .headline {
    position: absolute;
    left: 0;
    top: 620px;
    width: 1200px;
  }
  .headline-top {
    position: absolute;
    left: 188px;
    top: 0;
    font-size: 152px;
    line-height: 1;
    white-space: nowrap;
  }
  .headline-top .pre { color: var(--sky-blue); font-weight: 400; }
  .headline-top .qualify { color: var(--sun-yellow); font-weight: 700; }
  .for-badge {
    position: absolute;
    left: 92px;
    top: 148px;
    width: 216px;
    height: 216px;
    border-radius: 50%;
    background: var(--button-blue);
    color: var(--sun-yellow);
    font-weight: 700;
    font-size: 96px;
    display: flex;
    align-items: center;
    justify-content: center;
    padding-bottom: 10px;
  }
  .headline-rest {
    position: absolute;
    left: 336px;
    top: 200px;
    color: var(--white);
    font-size: 82px;
    font-weight: 400;
    white-space: nowrap;
  }
  .divider {
    position: absolute;
    left: 432px;
    top: 1082px;
    width: 328px;
    height: 4px;
    background: var(--divider);
  }
  .cta-button {
    position: absolute;
    left: 304px;
    top: 1244px;
    width: 592px;
    height: 160px;
    background: var(--button-blue);
    color: var(--white);
    font-weight: 700;
    font-size: 64px;
    display: flex;
    align-items: center;
    justify-content: center;
    text-decoration: none;
    border-radius: 4px;
  }
  .site-url {
    position: absolute;
    left: 0;
    top: 1440px;
    width: 1200px;
    text-align: center;
    color: var(--url-grey);
    font-size: 40px;
    letter-spacing: 7px;
  }
  .coast-scene {
    position: absolute;
    left: 0;
    bottom: 0;
    width: 1200px;
    height: 640px;
  }
</style>
</head>
<body>
  <main class="banner">
    <header class="brand-header">
      <span class="brand-dot" aria-hidden="true"></span>
      <div class="brand-name">Brightvale<br>Mortgage</div>
    </header>

    <h1 class="headline">
      <span class="headline-top"><span class="pre">Pre-</span><span class="qualify">Qualify</span></span>
      <span class="for-badge">for</span>
      <span class="headline-rest">a home loan today</span>
    </h1>

    <div class="divider" aria-hidden="true"></div>

    <a class="cta-button" href="#">Click Here</a>
    <p class="site-url">brightvalemortgage.example</p>

    <svg class="coast-scene" viewBox="0 0 1200 640" role="img" aria-label="Illustration of blue mountain peaks framing a sunny beach with waves, a rising yellow sun and seagulls">
      <defs>
        <linearGradient id="coast-fill" x1="0" y1="0" x2="0" y2="1">
          <stop offset="0" stop-color="#4ab3ea"/>
          <stop offset="0.5" stop-color="#7fb9cf"/>
          <stop offset="1" stop-color="#c9b79a"/>
        </linearGradient>
      </defs>
      <rect x="0" y="0" width="1200" height="640" fill="url(#coast-fill)"/>
    </svg>
  </main>
</body>
</html>
```